Business Card Layout for a Staffing Company
Brightmoor Consulting Group
Simple
Mark Dellinger
President
27 Quillhaven Road, Suite 410
Alder Cove, Vermont 11783
mdellinger@brightmoorconsulting.com
brightmoorconsulting.com

```html
<!DOCTYPE html>
<html lang="en">
<head>
<meta charset="utf-8">
<title>Brightmoor Consulting Group – Business Card</title>
<link rel="stylesheet" href="https://fonts.googleapis.com/css2?family=Cinzel:wght@400;600&display=swap">
<style>
  :root {
    --bg: #e9ebea;
    --green-dark: #0b5a44;
    --green: #12785b;
    --green-light: #2fa283;
    --paper: #ffffff;
    --paper-shade: #eef0ef;
    --ink: #3f4a47;
    --ink-soft: #6b7572;
    --rule: #9aa5a1;
  }
  * { box-sizing: border-box; margin: 0; padding: 0; }
  html, body { width: 1200px; height: 901px; overflow: hidden; }
  body {
    background: var(--bg);
    font-family: "Cinzel", "Times New Roman", serif;
    position: relative;
  }
  .card {
    position: absolute;
    width: 560px;
    height: 320px;
    border-radius: 22px;
    overflow: hidden;
    box-shadow: 0 14px 30px rgba(0,0,0,0.18);
  }
  .card--back {
    left: 110px; top: 90px;
    background: linear-gradient(135deg, var(--green-light) 0%, var(--green) 45%, var(--green-dark) 100%);
    color: var(--paper);
  }
  .back-mark {
    position: absolute; left: 0; right: 0; top: 92px;
    display: flex; align-items: center; justify-content: center; gap: 16px;
  }
  .back-mark__dot { width: 54px; height: 54px; border-radius: 50%; background: var(--paper); }
  .back-mark__name { font-size: 34px; font-weight: 400; letter-spacing: 2px; }
  .back-url {
    position: absolute; left: 0; right: 0; bottom: 34px;
    text-align: center; font-size: 13px; letter-spacing: 7px; text-transform: uppercase;
    color: rgba(255,255,255,0.85);
  }
  .card--front {
    left: 530px; top: 470px;
    background: linear-gradient(180deg, var(--paper) 0%, var(--paper-shade) 100%);
    color: var(--ink);
  }
  .front-mark {
    position: absolute; left: 0; right: 0; top: 38px;
    display: flex; align-items: center; justify-content: center; gap: 12px;
  }
  .front-mark__dot { width: 44px; height: 44px; border-radius: 50%; background: var(--green); }
  .front-mark__name { color: var(--green); font-weight: 600; line-height: 1.05; }
  .front-mark__name .word { display: block; font-size: 32px; letter-spacing: 1px; }
  .front-mark__name .sub { display: block; font-size: 12.5px; letter-spacing: 1.5px; }
  .details {
    position: absolute; left: 22px; right: 16px; top: 140px;
    display: flex; align-items: flex-start;
  }
  .person { width: 208px; flex: none; text-align: right; padding-right: 16px; padding-top: 4px; }
  .person__name { color: var(--green); font-size: 16px; font-weight: 600; letter-spacing: 1px; white-space: nowrap; }
  .person__title { color: var(--ink-soft); font-size: 12px; letter-spacing: 1.5px; margin-top: 4px; }
  .divider { width: 1px; height: 92px; background: var(--rule); flex: none; }
  .contact { padding-left: 14px; font-size: 11px; line-height: 1.55; letter-spacing: 0.3px; color: var(--ink); white-space: nowrap; }
  .contact__row { display: flex; align-items: center; gap: 6px; }
  .contact__row svg { width: 11px; height: 11px; fill: var(--ink); flex: none; }
  .front-band {
    position: absolute; left: 0; right: 0; bottom: 0; height: 58px;
    background: linear-gradient(180deg, var(--green-light) 0%, var(--green) 60%, var(--green-dark) 100%);
    display: flex; align-items: center; justify-content: center;
    color: var(--paper); font-size: 13px; letter-spacing: 6px; text-transform: uppercase;
  }
</style>
</head>
<body>

  <section class="card card--back" aria-label="Card back">
    <div class="back-mark">
      <span class="back-mark__dot"></span>
      <span class="back-mark__name">Brightmoor</span>
    </div>
    <p class="back-url">www.brightmoorconsulting.com</p>
  </section>

  <section class="card card--front" aria-label="Card front">
    <div class="front-mark">
      <span class="front-mark__dot"></span>
      <span class="front-mark__name">
        <span class="word">BRIGHTMOOR</span>
        <span class="sub">Consulting Group</span>
      </span>
    </div>

    <div class="details">
      <div class="person">
        <p class="person__name">MARK DELLINGER</p>
        <p class="person__title">PRESIDENT</p>
      </div>
      <div class="divider"></div>
      <div class="contact">
        <p>27 Quillhaven Road, Suite 410</p>
        <p>Alder Cove, Vermont 11783</p>
        <p class="contact__row">
          <svg viewBox="0 0 24 24" aria-hidden="true"><path d="M6.6 10.8a15.1 15.1 0 0 0 6.6 6.6l2.2-2.2c.3-.3.7-.4 1-.2 1.1.4 2.3.6 3.6.6.6 0 1 .4 1 1V20c0 .6-.4 1-1 1A17 17 0 0 1 3 4c0-.6.4-1 1-1h3.5c.6 0 1 .4 1 1 0 1.3.2 2.5.6 3.6.1.3 0 .7-.2 1z"/></svg>
          555 310-0148
        </p>
        <p class="contact__row">
          <svg viewBox="0 0 24 24" aria-hidden="true"><path d="M6 3h9v5H6zM4 9h16a2 2 0 0 1 2 2v6h-4v4H6v-4H2v-6a2 2 0 0 1 2-2zm4 7v3h8v-3z"/></svg>
          555 310-0172
        </p>
        <p class="contact__row">
          <svg viewBox="0 0 24 24" aria-hidden="true"><path d="M2 5h20v14H2zm2 2v.5l8 5 8-5V7zm0 2.8V17h16V9.8l-8 5z"/></svg>
          mdellinger@brightmoorconsulting.com
        </p>
      </div>
    </div>

    <div class="front-band">www.brightmoorconsulting.com</div>
  </section>

</body>
</html>
```